Drug safety monitoring company requires a new corporate website

We are an outsourcing partner to large and small companies within the pharmaceutical industry. Our current website www.quorvanta.co.uk has not been updated in a long time. We want a new web site that is responsive and modern but with a clearly corporate and professional feel. We want a design based on a 12 column grid system (mobile and desktop version). We want to use a new, modern font (not the standard web fonts) - we will purchase as required. Content can be used as is from the current website. Red and white are the corporate colours, so a palate should be developed to match. We do not need as much red as is in the current website. New icons (preferably in svg format) would be great. We can also purchase new images from Framly (or other) as required. We would prefer submissions in Sketch if possible.

Target Market(s)

Pharmaceutical companies

Number of Pages Required

1 page

Font styles to use
Sans Serif

Colors
ec1f27
ffffff

Requirements
Must have
• Design based on 12 column grid system.
Responsive design (i.e. require a mobile and desktop version).
How should the menu look between desktop and mobile?
A coherent colour palete.
Content to come from the existing website: www.quorvanta.co.uk
How should links be styled?
How should headings, sub-headings, paragraphs be styled?
Nice to have
• Custom developed icons (these are along the bottom of the page on the existing website: Medical Information; Pharmacovigilance; Literature Monitoring; Training).
New imagery (the images on the current website are dated).
Submission ideally as Sketch files (but we are okay with photoshop too).
A new, modern, non-standard font.
Not so much red in the design.
If we had buttons on the website, how should they be styled?
If we had a form on the website, how should the fields be styled?

```html
<!DOCTYPE html>
<html lang="en">
<head>
<meta charset="utf-8">
<title>Quorvanta – Pharmacovigilance</title>
<link rel="stylesheet" href="https://fonts.googleapis.com/css2?family=Montserrat:wght@400;500&family=DM+Sans:wght@400;500;700&display=swap">
<style>
:root{
  --red:#ec3a3c;
  --red-deep:#ec1f27;
  --white:#ffffff;
  --page:#f2f3f8;
  --soft:#f6f7fb;
  --navy:#1b2a4e;
  --text:#3c4560;
  --muted:#9aa1b3;
  --line:#e4e6ee;
  --green:#4cd964;
  --blue:#3f7cf0;
  --yellow:#f7c531;
}
*{margin:0;padding:0;box-sizing:border-box}
html,body{width:1200px;height:3128px;overflow:hidden}
body{background:var(--page);font-family:"DM Sans",sans-serif;color:var(--text);position:relative}
.abs{position:absolute}
.heading{font-family:"Montserrat",sans-serif;font-weight:400;color:var(--navy)}
.eyebrow{font-size:14px;color:var(--red);letter-spacing:.3px;text-transform:uppercase}

/* hero */
.hero-side{left:0;top:0;width:1200px;height:753px;background:var(--soft)}
.hero-red{left:0;top:0;width:907px;height:807px;background:var(--red);border-bottom-right-radius:300px}
.logo{display:flex;align-items:center;gap:6px;font-family:"DM Sans",sans-serif;font-weight:700;font-size:19px}
.logo .mark{width:14px;height:14px;border:2px solid currentColor;border-radius:3px}
.hero .logo{left:87px;top:68px;color:var(--white)}
.btn{display:flex;align-items:center;justify-content:center;font-size:16px;text-decoration:none}
.btn-outline{border:1px solid var(--white);color:var(--white)}
.btn-solid{background:var(--white);color:var(--red)}
.nav-contact{left:728px;top:51px;width:126px;height:40px;font-size:12px;border-color:rgba(255,255,255,.8)}
.menu-btn{left:1054px;top:52px;width:36px;height:36px;border-radius:50%;background:var(--red);display:flex;flex-direction:column;justify-content:center;align-items:center;gap:3px}
.menu-btn span{width:12px;height:1.5px;background:var(--white)}
.hero-title{left:88px;top:242px;width:540px;font-size:38px;line-height:52.5px;color:var(--white)}
.hero-contact{left:95px;top:486px;width:176px;height:62px}
.hero-learn{left:287px;top:486px;width:176px;height:62px}
.hero-photo{left:645px;top:198px;width:488px;height:488px;border-radius:50%;background:radial-gradient(circle at 45% 45%,#c7ccd4,#8a97a8 55%,#dfe3e8)}

/* about */
.about-panel{left:756px;top:896px;width:444px;height:509px;background:var(--white)}
.about-eyebrow{left:87px;top:1033px}
.about-title{left:87px;top:1064px;width:460px;font-size:33px;line-height:46px}
.about-text{left:87px;top:1172px;width:470px;font-size:18px;line-height:30.5px}
.about-text p+p{margin-top:15px}
.ph{border-radius:2px}
.ph-lab{left:622px;top:972px;width:210px;height:251px;background:linear-gradient(160deg,#d7dde4,#eef1f4 50%,#9aa7b6)}
.ph-tablet{left:839px;top:972px;width:212px;height:177px;background:linear-gradient(150deg,#dfe3e8,#c3c9d1)}
.ph-glove{left:911px;top:1155px;width:140px;height:191px;background:linear-gradient(170deg,#dde4ec,#7aa0d6 70%,#cfd8e2)}
.badge-red{left:855px;top:1167px;width:40px;height:40px;border-radius:50%;background:var(--red);display:flex;align-items:center;justify-content:center}
.badge-red i{width:14px;height:12px;border:1.5px solid var(--white);border-radius:2px}
.quote-card{left:623px;top:1233px;width:281px;height:113px;background:var(--white);box-shadow:0 6px 20px rgba(30,40,80,.08)}
.quote-card .avatar{position:absolute;left:23px;top:35px;width:38px;height:38px;border-radius:50%;background:#5a5f68}
.quote-card p{position:absolute;left:80px;top:34px;width:185px;font-size:13px;line-height:18.5px;color:var(--navy)}
.quote-card small{position:absolute;left:80px;top:77px;font-size:10px;color:var(--muted)}
.quote-card .qm{position:absolute;right:26px;top:10px;font-family:"Montserrat",sans-serif;font-size:18px;color:#c9ccd6}
.pager{left:684px;top:1373px;display:flex;gap:8px}
.pager span{width:7px;height:7px;border-radius:50%;background:#f5a3a4}
.pager span:first-child{background:var(--red)}

/* services */
.svc-eyebrow{left:87px;top:1498px}
.svc-title{left:87px;top:1525px;font-size:33px}
.arrow{width:32px;height:32px;border-radius:50%;border:1px solid var(--navy);display:flex;align-items:center;justify-content:center}
.svc-prev{left:1036px;top:1525px}
.svc-next{left:1080px;top:1525px}
.card{top:1625px;width:271px;height:198px;background:var(--white);border-radius:12px;border:1px solid var(--line);box-shadow:0 6px 20px rgba(30,40,80,.05);padding:39px 14px 0 28px}
.card h3{display:flex;align-items:center;gap:15px;font-size:15.5px;font-weight:500;color:var(--navy);white-space:nowrap}
.card h3 i{width:40px;height:40px;border-radius:50%;flex:none;display:flex;align-items:center;justify-content:center}
.card h3 i::after{content:"";width:12px;height:12px;border:1.5px solid var(--white);border-radius:2px}
.card p{margin-top:21px;font-size:14px;line-height:21px;color:var(--navy)}
.card-fade{opacity:.55}

/* testimonial */
.quote-circle{left:109px;top:2036px;width:170px;height:170px;border-radius:50%;background:var(--red);display:flex;align-items:center;justify-content:center;font-family:"Montserrat",sans-serif;font-weight:500;font-size:96px;color:var(--white);line-height:1;padding-top:40px}
.testi-card{left:361px;top:1943px;width:759px;height:354px;background:var(--white);border-radius:16px}
.testi-text{left:453px;top:2023px;width:600px;font-size:24px;line-height:36.5px;color:var(--text)}
.testi-avatar{left:452px;top:2196px;width:46px;height:46px;border-radius:50%;background:linear-gradient(150deg,#8fa07a,#5c6f83)}
.testi-name{left:519px;top:2197px;font-size:18px;color:var(--navy)}
.testi-role{left:519px;top:2222px;font-size:13px;color:var(--muted)}
.testi-prev{left:931px;top:2278px;width:40px;height:40px;background:var(--white)}
.testi-next{left:986px;top:2278px;width:40px;height:40px;background:var(--white)}

/* cta */
.cta{left:0;top:2406px;width:1200px;height:311px;background:var(--red)}
.ring{border:2px solid var(--white);border-radius:50%;display:flex;align-items:center;justify-content:center}
.ring-sm{left:75px;top:2467px;width:42px;height:42px}
.ring-md{left:222px;top:2563px;width:68px;height:68px}
.ring-lg{left:1008px;top:2480px;width:113px;height:113px}
.cta-eyebrow{left:0;top:2486px;width:1196px;text-align:center;font-size:13px;color:var(--white)}
.cta-title{left:0;top:2513px;width:1192px;text-align:center;font-size:31px;color:var(--white);font-weight:500}
.cta-btn{left:510px;top:2576px;width:178px;height:61px}

/* footer */
.footer-bg{left:0;top:2717px;width:1200px;height:411px;background:var(--soft)}
.footer .logo{left:86px;top:2806px;color:var(--red)}
.fcol{top:2806px;font-size:12.5px;color:var(--navy)}
.fcol h4{font-weight:700;font-size:12.5px;margin-bottom:17px}
.fcol li{list-style:none;margin-bottom:13.5px}
.col-nav{left:357px}
.col-prod{left:482px}
.col-addr{left:607px}
.col-addr li{margin-bottom:14px}
.phone-pill{left:607px;top:2907px;width:191px;height:37px;background:var(--white);border-radius:6px;box-shadow:0 4px 14px rgba(30,40,80,.06);display:flex;align-items:center;gap:8px;padding-left:14px;font-size:6px;color:var(--muted)}
.phone-pill i{width:14px;height:14px;border-radius:50%;background:#29c4d8}
.phone-pill b{font-size:10.5px;letter-spacing:2px;color:var(--navy);font-weight:700}
.col-social{left:878px}
.social{top:2851px;width:44px;height:44px;border-radius:50%;background:var(--navy)}
.social.hot{background:var(--red);box-shadow:0 6px 14px rgba(236,58,60,.35)}
.copy{left:0;top:3066px;width:1200px;text-align:center;font-size:11px;color:var(--navy)}
.copy small{display:block;margin-top:6px;font-size:8px}
</style>
</head>
<body>

<header class="hero">
  <div class="abs hero-side"></div>
  <div class="abs hero-red"></div>
  <div class="abs logo"><span class="mark"></span>Quorvanta.</div>
  <a class="abs btn btn-outline nav-contact">Contact us</a>
  <div class="abs menu-btn"><span></span><span></span><span></span></div>
  <h1 class="abs heading hero-title" style="color:var(--white)">Quorvanta ensure that your business has the best Pharmacovigilance support in the industry.</h1>
  <a class="abs btn btn-solid hero-contact">Contact us</a>
  <a class="abs btn btn-outline hero-learn">Learn more</a>
  <div class="abs hero-photo" role="img" aria-label="Three scientists in lab coats examining a sample with blue gloves"></div>
</header>

<section class="about">
  <div class="abs about-panel"></div>
  <p class="abs eyebrow about-eyebrow">About us</p>
  <h2 class="abs heading about-title">Welcome to the Quorvanta Pharmacovigilance</h2>
  <div class="abs about-text">
    <p>We are an outsourcing partner to large and small companies within the pharmaceutical industry.</p>
    <p>Our range of services is tailored to suit each of our client’s needs and cover both human and veterinary medicinal products.</p>
  </div>
  <div class="abs ph ph-lab" role="img" aria-label="Scientist in a lab coat and safety glasses standing in a laboratory"></div>
  <div class="abs ph ph-tablet" role="img" aria-label="Hands using a tablet with a stylus"></div>
  <div class="abs ph ph-glove" role="img" aria-label="Gloved hand working with lab samples"></div>
  <div class="abs badge-red"><i></i></div>
  <div class="abs quote-card">
    <span class="avatar"></span>
    <span class="qm">”</span>
    <p>Quorvanta is exactly what our business has been lacking.</p>
    <small>Tamsin R.</small>
  </div>
  <div class="abs pager"><span></span><span></span><span></span></div>
</section>

<section class="services">
  <p class="abs eyebrow svc-eyebrow">Our services</p>
  <h2 class="abs heading svc-title">Quorvanta Quality services</h2>
  <div class="abs arrow svc-prev"><svg width="12" height="8" viewBox="0 0 12 8"><path d="M11 4H1M4 1L1 4l3 3" fill="none" stroke="#1b2a4e" stroke-width="1.2"/></svg></div>
  <div class="abs arrow svc-next"><svg width="12" height="8" viewBox="0 0 12 8"><path d="M1 4h10M8 1l3 3-3 3" fill="none" stroke="#1b2a4e" stroke-width="1.2"/></svg></div>
  <article class="abs card" style="left:89px"><h3><i style="background:var(--green)"></i>Medical Information</h3><p>Professional enquiry handling to support the safe and effective use of your products.</p></article>
  <article class="abs card" style="left:398px"><h3><i style="background:var(--red)"></i>Pharmacovigilance</h3><p>Ease the regulatory burden and keep compliant with current pharmacovigilance legislation.</p></article>
  <article class="abs card" style="left:713px"><h3><i style="background:var(--blue)"></i>Literature Monitoring</h3><p>Product safety through the surveillance of published articles and case reports.</p></article>
  <article class="abs card card-fade" style="left:1028px"><h3><i style="background:var(--yellow)"></i>Training</h3><p>Confident staff to support pharmacovigilance processes.</p></article>
</section>

<section class="testimonial">
  <div class="abs quote-circle">”</div>
  <div class="abs testi-card"></div>
  <p class="abs testi-text">Quorvanta is the most valuable business resource we have ever purchased. Quorvanta was the best investment I ever made. Quorvanta's got you covered. We have no regrets!</p>
  <div class="abs testi-avatar" role="img" aria-label="Portrait of the reviewer"></div>
  <p class="abs testi-name">Marissa Holt</p>
  <p class="abs testi-role">Care team</p>
  <div class="abs arrow testi-prev"><svg width="14" height="9" viewBox="0 0 12 8"><path d="M11 4H1M4 1L1 4l3 3" fill="none" stroke="#1b2a4e" stroke-width="1.2"/></svg></div>
  <div class="abs arrow testi-next"><svg width="14" height="9" viewBox="0 0 12 8"><path d="M1 4h10M8 1l3 3-3 3" fill="none" stroke="#1b2a4e" stroke-width="1.2"/></svg></div>
</section>

<section class="cta-section">
  <div class="abs cta"></div>
  <div class="abs ring ring-sm"><svg width="14" height="14" viewBox="0 0 14 14"><path d="M3 12h8M5 12V4l3-2v10" fill="none" stroke="#fff" stroke-width="1.3"/></svg></div>
  <div class="abs ring ring-md"><svg width="28" height="24" viewBox="0 0 28 24"><rect x="2" y="5" width="24" height="17" rx="3" fill="none" stroke="#fff" stroke-width="2"/><path d="M10 5V2h8v3M14 9v9M9.5 13.5h9" fill="none" stroke="#fff" stroke-width="2"/></svg></div>
  <div class="abs ring ring-lg"><svg width="40" height="34" viewBox="0 0 40 34"><path d="M20 31S3 21 3 10a8.5 8.5 0 0 1 17-2 8.5 8.5 0 0 1 17 2c0 11-17 21-17 21z" fill="none" stroke="#fff" stroke-width="2.4"/><path d="M7 16h8l2-4 3 8 2-4h11" fill="none" stroke="#fff" stroke-width="2.4"/></svg></div>
  <p class="abs cta-eyebrow">READY TO GET STARTED ?</p>
  <h2 class="abs heading cta-title" style="color:var(--white)">Get in touch with us</h2>
  <a class="abs btn btn-solid cta-btn">Contact us</a>
</section>

<footer class="footer">
  <div class="abs footer-bg"></div>
  <div class="abs logo"><span class="mark"></span>Quorvanta.</div>
  <div class="abs fcol col-nav"><h4>Navigation</h4><ul><li>Home</li><li>About us</li><li>Client</li><li>Contact</li></ul></div>
  <div class="abs fcol col-prod"><h4>Product</h4><ul><li>Services</li><li>Testimonial</li><li>Qppv</li><li>Privacy Policy</li></ul></div>
  <div class="abs fcol col-addr"><h4>Adress</h4><ul><li>14 Mill Lane, England UK.</li><li>info@quorvanta.co.uk</li></ul></div>
  <div class="abs phone-pill"><i></i>Call us on <b>0330-2741-508</b></div>
  <div class="abs fcol col-social"><h4>Social Media</h4></div>
  <span class="abs social" style="left:878px"></span>
  <span class="abs social hot" style="left:940px"></span>
  <span class="abs social" style="left:997px"></span>
  <p class="abs copy">© Quorvanta Company - All Rights Reserved<small>Terms &amp; Conditions | Privacy Policy | Contact Us</small></p>
</footer>

</body>
</html>
```